Tove & Lark Designs - Promotions flyer

I am a locally based Interior designer /stylist on Sydney's lower north shore. I would like to offer my services:
Full Professional Styling Services and Furniture Hire
Colour Consultation – Interior / exterior
Floor Coverings
Furniture selection and sourcing
Window Treatments
Wallpaper
Soft Furnishings
Upholstery
Renovations

I would like to offer a free consultation
Updates

Project Deadline Extended
Reason: I've been speaking with a designer and need her to make one more change. I have tried to message her twice, but have had no reply. Once she makes these changes I'm ready to sign off on the design. Thanks Harriet

Target Market(s)

30 - 60's middle to high income earners

Industry/Entity Type

Floor

Requirements
Must have
• one sided DL size
Use my logo
1 or 2 images of interior space or image of a lamp, cushion, lounge etc
The following contact details:
Mobile: 041 xxx xxxx
Website Address: www.tovelarkdesigns.example.au

```html
<!DOCTYPE html>
<html lang="en">
<head>
<meta charset="UTF-8">
<title>Tove &amp; Lark Designs – Promotions Flyer</title>
<link rel="stylesheet" href="https://fonts.googleapis.com/css2?family=Open+Sans:wght@400;600;700&family=Signika:wght@600&display=swap">
<style>
  :root {
    --page-bg: #e8e5e0;
    --charcoal: #26272a;
    --charcoal-deep: #1b1c1e;
    --orange: #f7931e;
    --white: #ffffff;
    --wall-top: #ddd1b6;
    --wall-bottom: #cbbd9e;
    --floor-top: #9c7c5e;
    --floor-bottom: #6e5240;
    --ink: #1c1c1c;
  }
  * { margin: 0; padding: 0; box-sizing: border-box; }
  html, body {
    width: 1200px; height: 750px; overflow: hidden;
    background: var(--page-bg);
    font-family: "Open Sans", Arial, sans-serif;
  }
  .flyer {
    position: absolute; left: 70px; top: 125px;
    width: 1060px; height: 500px;
    background: linear-gradient(160deg, var(--charcoal), var(--charcoal-deep));
    overflow: hidden;
    box-shadow: 0 10px 30px rgba(0,0,0,.25);
  }
  .flyer-shapes { position: absolute; inset: 0; }
  .room-image { position: absolute; left: 0; top: 0; width: 770px; height: 395px; }
  .brand-name {
    position: absolute; left: 0; top: 125px; width: 770px;
    text-align: center;
    font-family: "Open Sans", Arial, sans-serif;
    font-weight: 600; font-size: 46px; color: var(--charcoal);
    letter-spacing: -0.5px;
  }
  .offer-ribbon-text {
    position: absolute; left: 4px; top: 34px;
    width: 150px; transform: rotate(-45deg);
    text-align: center; color: var(--white);
    font-family: "Signika", Arial, sans-serif; font-weight: 600;
    line-height: 1.05;
  }
  .offer-ribbon-text .free { display: block; font-size: 18px; }
  .offer-ribbon-text .consult { display: block; font-size: 17px; }
  .contact-bar {
    position: absolute; left: 60px; top: 405px;
    font-size: 17px; font-weight: 600; color: var(--ink);
    letter-spacing: .2px;
  }
  .contact-bar .sep { margin: 0 10px; }
  .services {
    position: absolute; left: 800px; top: 110px; width: 240px;
    color: var(--white);
  }
  .services-title {
    font-family: "Signika", Arial, sans-serif; font-weight: 600;
    font-size: 26px; color: var(--orange); letter-spacing: 1px;
    margin-bottom: 6px;
  }
  .services-list { list-style: none; }
  .services-list li {
    position: relative; padding-left: 18px;
    font-size: 15px; line-height: 1.3; margin-bottom: 4px;
  }
  .services-list li::before {
    content: ""; position: absolute; left: 2px; top: 7px;
    width: 6px; height: 6px; border-radius: 50%; background: var(--orange);
  }
</style>
</head>
<body>
  <article class="flyer">
    <svg class="flyer-shapes" width="1060" height="500" viewBox="0 0 1060 500" aria-hidden="true">
      <path d="M0 380 H760 V395 Q760 445 720 445 H0 Z" fill="var(--orange)"/>
    </svg>

    <svg class="room-image" viewBox="0 0 770 395" role="img" aria-label="Interior photo: stone-textured feature wall with two black picture frames, a black floor lamp and a timber floor">
      <defs>
        <linearGradient id="room-tones" x1="0" y1="0" x2="0" y2="1">
          <stop offset="0" stop-color="var(--wall-top)"/>
          <stop offset="0.62" stop-color="var(--wall-bottom)"/>
          <stop offset="0.7" stop-color="var(--floor-top)"/>
          <stop offset="1" stop-color="var(--floor-bottom)"/>
        </linearGradient>
      </defs>
      <rect width="770" height="395" fill="url(#room-tones)"/>
    </svg>

    <svg class="flyer-shapes" width="1060" height="500" viewBox="0 0 1060 500" aria-hidden="true">
      <polygon points="0,95 95,0 165,0 0,165" fill="var(--orange)"/>
    </svg>
    <div class="offer-ribbon-text">
      <span class="free">FREE</span>
      <span class="consult">Consultation!</span>
    </div>

    <p class="brand-name">Tove &amp; Lark Designs</p>

    <p class="contact-bar">CALL : 041 xxx xxxx<span class="sep">|</span>www.tovelarkdesigns.example.au</p>

    <section class="services">
      <h2 class="services-title">SERVICES:</h2>
      <ul class="services-list">
        <li>Full Professional Styling Services and Furniture Hire</li>
        <li>Colour Consultation –<br>Interior / exterior</li>
        <li>Floor Coverings</li>
        <li>Furniture selection and sourcing</li>
        <li>Window Treatments</li>
        <li>Wallpaper</li>
        <li>Soft Furnishings</li>
        <li>Upholstery</li>
        <li>Renovations</li>
      </ul>
    </section>
  </article>
</body>
</html>
```